Esthetically Pleasing Core Values and Brand Promise for Accounting Firm

I would like a cohesive design that ties together my core values and brand promise. My firm, Maple Finch Advisory, provides accounting work to small businesses. I prefer modern and clean designs. I want my Core Values and Brand Promise to represent me - sole entrepreneur, married, mother of two kids, modern esthetics, clean lines, organized, colorful (teals, greys, white, yellows)

Industry/Entity Type

Public Accounting

Colors
33b8a4

```html
<!DOCTYPE html>
<html lang="en">
<head>
<meta charset="UTF-8">
<title>Maple Finch Advisory – Core Values &amp; Brand Promise</title>
<link href="https://fonts.googleapis.com/css2?family=Montserrat:wght@300;500;600;700;800&family=Barlow+Condensed:wght@500&display=swap" rel="stylesheet">
<style>
  :root{
    --teal:#1b9e98;
    --teal-deep:#1f7f78;
    --teal-light:#35a8a0;
    --paper:#f3f4f6;
    --mist:#e3e5e8;
    --ink:#2b2f33;
    --white:#ffffff;
  }
  *{margin:0;padding:0;box-sizing:border-box}
  html,body{width:889px;height:1200px;overflow:hidden;background:var(--paper)}
  .flyer{position:relative;width:889px;height:1200px;background:var(--paper);font-family:'Montserrat',sans-serif;color:var(--ink)}
  .hero{position:absolute;left:0;top:0;width:889px;height:560px}
  .brand-name{position:absolute;left:44px;top:318px;color:var(--white);font-family:'Montserrat',sans-serif;font-weight:300;line-height:1}
  .brand-name .line{display:block;font-size:62px;letter-spacing:6px}
  .brand-name .line + .line{margin-top:10px}
  .brand-name .sub{display:block;font-size:31px;letter-spacing:4px;margin-top:22px}

  .values{position:absolute;left:71px;top:612px;width:440px}
  .values-title{font-weight:800;font-size:40px;color:var(--teal);letter-spacing:0.5px;line-height:1.1}
  .values-rule{width:117px;height:3px;background:var(--teal);margin-top:4px}
  .value{position:absolute;left:0;width:440px}
  .value-icon{position:absolute;left:0;width:104px;height:104px}
  .value-text{position:absolute;left:122px;width:320px}
  .value-name{font-weight:600;font-size:21px;color:var(--teal);line-height:1.1;margin-bottom:3px}
  .value-desc{font-weight:500;font-size:15.5px;line-height:21px;color:var(--ink)}

  .promise{position:absolute;left:560px;top:612px;width:257px;height:525px;background:var(--teal);color:var(--white);padding:42px 10px 0 23px}
  .promise-title{font-weight:700;font-size:23.5px;line-height:31px;letter-spacing:0.3px}
  .service{margin-top:30px}
  .service + .service{margin-top:14px}
  .service-name{font-weight:700;font-size:25px;line-height:1.1}
  .service-rule{width:111px;height:2px;background:var(--white);margin:8px 0 6px}
  .service-desc{font-family:'Barlow Condensed',sans-serif;font-weight:500;font-size:19px;line-height:22px}

  .footer-band{position:absolute;left:0;bottom:0;width:889px;height:21px;background:var(--teal)}
</style>
</head>
<body>
<main class="flyer">
  <svg class="hero" viewBox="0 0 889 560" xmlns="http://www.w3.org/2000/svg">
    <defs>
      <linearGradient id="photoTone" x1="0" y1="0" x2="1" y2="1">
        <stop offset="0" stop-color="#c8c1ae"/>
        <stop offset="0.4" stop-color="#e7eaec"/>
        <stop offset="1" stop-color="#d5dfe6"/>
      </linearGradient>
      <linearGradient id="waveTone" x1="0" y1="0" x2="1" y2="0">
        <stop offset="0" stop-color="var(--teal-deep)"/>
        <stop offset="1" stop-color="var(--teal-light)"/>
      </linearGradient>
    </defs>
    <path role="img" aria-label="Photo of an accountant at a desk writing on financial charts and using a calculator"
          d="M300,0 L889,0 L889,470 C820,515 720,535 640,527 C450,505 330,385 302,235 C288,150 290,60 300,0 Z"
          fill="url(#photoTone)"/>
    <path d="M0,262 C120,236 250,222 330,225 L350,262 L0,290 Z" fill="var(--mist)"/>
    <path d="M0,570 C240,560 420,480 475,380" fill="none" stroke="var(--white)" stroke-width="22"/>
    <path d="M0,284 C140,262 290,246 360,256 C455,270 487,318 470,370 C440,450 260,545 0,557 Z" fill="url(#waveTone)"/>
  </svg>

  <div class="brand-name" aria-label="Maple Finch Advisory">
    <span class="line">MAPLE</span>
    <span class="line">FINCH</span>
    <span class="sub">ADVISORY</span>
  </div>

  <section class="values">
    <h2 class="values-title">CORE VALUES</h2>
    <div class="values-rule"></div>

    <div class="value" style="top:70px">
      <svg class="value-icon" viewBox="0 0 104 104" fill="none" stroke="var(--teal)" stroke-width="2.5" stroke-linecap="round" stroke-linejoin="round">
        <circle cx="52" cy="52" r="49" stroke-width="4"/>
        <path d="M38,44 v-6 a4,4 0 0 1 8,0 v-3 a4,4 0 0 1 8,0 v1 a4,4 0 0 1 8,0 v2 a4,4 0 0 1 8,0 v14 c0,8 -4,12 -8,14 v12 h-18 v-10 c-4,-3 -6,-8 -6,-14 z"/>
        <path d="M46,38 v8 M54,36 v10 M62,38 v8"/>
        <path d="M52,20 v4 M40,23 l2,4 M64,23 l-2,4 M31,31 l3,3 M73,31 l-3,3"/>
      </svg>
      <div class="value-text" style="top:7px">
        <h3 class="value-name">Empower</h3>
        <p class="value-desc">we are dedicated, appreciative and respectful of people’s time and purpose.</p>
      </div>
    </div>

    <div class="value" style="top:190px">
      <svg class="value-icon" viewBox="0 0 104 104" fill="none" stroke="var(--teal)" stroke-width="2.5" stroke-linecap="round">
        <circle cx="52" cy="52" r="49" stroke-width="4"/>
        <circle cx="52" cy="52" r="30"/>
        <circle cx="52" cy="52" r="24"/>
        <path d="M52,16 v14 M52,74 v14 M16,52 h14 M74,52 h14"/>
        <circle cx="52" cy="46" r="6"/>
        <path d="M41,63 c0,-7 5,-10 11,-10 s11,3 11,10 z"/>
      </svg>
      <div class="value-text" style="top:5px">
        <h3 class="value-name">Client Focused</h3>
        <p class="value-desc">we provide a personal service that goes above the standards of professional care.</p>
      </div>
    </div>

    <div class="value" style="top:306px">
      <svg class="value-icon" viewBox="0 0 104 104" fill="none" stroke="var(--teal)" stroke-width="2.5" stroke-linecap="round" stroke-linejoin="round">
        <circle cx="52" cy="52" r="49" stroke-width="4"/>
        <circle cx="52" cy="24" r="3"/>
        <path d="M52,27 v47 M26,34 h52 M40,80 h24 M44,74 h16"/>
        <path d="M30,34 l-9,22 M30,34 l9,22 M20,56 a10,6 0 0 0 20,0 z"/>
        <path d="M74,34 l-9,22 M74,34 l9,22 M64,56 a10,6 0 0 0 20,0 z"/>
      </svg>
      <div class="value-text" style="top:6px;left:118px">
        <h3 class="value-name">Rectitude</h3>
        <p class="value-desc">we know the difference between what we have the right to do and what the right thing to do is.</p>
      </div>
    </div>

    <div class="value" style="top:425px">
      <svg class="value-icon" viewBox="0 0 104 104" fill="none" stroke="var(--teal)" stroke-linejoin="round">
        <circle cx="52" cy="52" r="49" stroke-width="4"/>
        <path d="M56,26 L38,56 H51 L47,80 L66,48 H53 Z" fill="var(--teal)" stroke-width="1"/>
      </svg>
      <div class="value-text" style="top:6px">
        <h3 class="value-name">Relentless</h3>
        <p class="value-desc">we believe that the longer we try to do our best, the better we become.</p>
      </div>
    </div>
  </section>

  <aside class="promise">
    <h2 class="promise-title">BRAND PROMISE<br>TRUST,<br>TRANSPARENCY<br>&amp; DEPENDABILITY</h2>
    <div class="service">
      <h3 class="service-name">TAX:</h3>
      <div class="service-rule"></div>
      <p class="service-desc">Maple Finch provides all clients with a trusted tax advisor who provides accuracy in all filings and ensures your compliance with all government agencies.</p>
    </div>
    <div class="service">
      <h3 class="service-name">ACCOUNTING:</h3>
      <div class="service-rule"></div>
      <p class="service-desc">Maple Finch provides all business owners with the financial visibility needed to foster growth and facilitate goals.</p>
    </div>
  </aside>

  <div class="footer-band"></div>
</main>
</body>
</html>
```